Gluten free flour; by LOAFMIRE

We are a specialised flour company and this project is to develop packaging for a very niche and upmarket lifestyle gluten free flour in plain and also in wholemeal ( two products and you can choose which one would you like to design and submit for review)

We believe in minimalistic yet easily acceptable Design that STANS OUT and catches the eye of the viewer on a busy shelve in a grocery store.
The product will be sold on our website, through Pellora, through Social Media and also through special campaigns together with Grainwell Alliance of Canada.

We are looking for a stand up bag with zip lock and tear notch size approx. 9 in wide x 13 inch tall x 4 inch gusset .

Our flour produces soft, pliable, moist and fluffy roti and tortillas. (Flour only not finished product).

We only manufacture Gluten free flour and flour related products and do not deal with wheat or wheat related products.

Website isn't an initial stage URL http://env.quorvane.example/loafmire Company name : Loafmire Inc

Target Market(s)

Canadian East Indian, Canadian-Latin Americans, Caucasian-Canadians and Americans who are gluten free by lifestyle choice or because of Celiac disease or Gluten Intolerance.

Industry/Entity Type

Manufacturing

Logo Text

Loafmire

Requirements
Must have
• Prominent "Gluten Free"
Emblems: 100% Organic, 100% Gluten free, Low GI, Vegan, Soy free, dairy free, allergens free, Grainwell Alliance
Roti graphics (picture)
Nice to have
• 0% Saturated Fat only 1% Total fat, Cholesterol Free, Very Low Sodium, Good Source of Dietary Fiber. Weight management. Perfect for Gluten free lifestyle. Organic ingredients
Graphics of grains (Sorghum, Buckwheat, Brown rice, Chickpeas)
Should not have
• Wheat or related to wheat graphics, Anything referring to Gluten. Too busy looking

```html
<!DOCTYPE html>
<html lang="en">
<head>
<meta charset="utf-8">
<title>Loafmire Plain Flour Gluten Free</title>
<link rel="stylesheet" href="https://fonts.googleapis.com/css2?family=Montserrat:wght@700;800&family=Oswald:wght@500&display=swap">
<style>
  :root {
    --paper: #ffffff;
    --blush: #f5b5b5;
    --rose: #d69aa0;
    --lilac: #dedbe8;
    --teal: #85a9aa;
    --mauve: #c79aa6;
    --peach: #efcfb1;
    --sorghum-light: #c8734a;
    --sorghum: #a9512e;
    --roti-light: #f2dca6;
    --roti: #e2bf80;
    --ink: #2e2e30;
    --panel: #3a3a3c;
    --panel-text: #ffffff;
  }
  * { margin: 0; padding: 0; box-sizing: border-box; }
  html, body { width: 886px; height: 1200px; overflow: hidden; background: var(--paper); }
  .package { position: relative; width: 886px; height: 1200px; overflow: hidden; background: var(--paper); }
  .backdrop { position: absolute; inset: 0; }
  .title-line {
    position: absolute; right: 294px; text-align: right; white-space: nowrap;
    font-family: "Montserrat", sans-serif; font-weight: 800; color: var(--ink); line-height: 1;
  }
  .title-plain { top: 736px; font-size: 47px; }
  .title-flour { top: 756px; font-size: 102px; letter-spacing: -2px; }
  .title-gf { top: 854px; font-size: 48px; }
  .benefits {
    position: absolute; right: 294px; top: 925px; text-align: right; white-space: nowrap;
    font-family: "Montserrat", sans-serif; font-weight: 700; font-size: 15.5px;
    line-height: 18.5px; color: var(--ink);
  }
  .net-weight {
    position: absolute; right: 294px; top: 1070px; text-align: right;
    font-family: "Montserrat", sans-serif; font-weight: 700; font-size: 16px;
    line-height: 22px; color: var(--ink);
  }
  .claims-panel {
    position: absolute; left: 617px; top: 720px; width: 269px; height: 480px;
    background: var(--panel); color: var(--panel-text);
    font-family: "Oswald", sans-serif; font-weight: 500;
  }
  .claims { list-style: none; position: absolute; left: 22px; top: 26px; }
  .claim { display: flex; align-items: center; height: 37.7px; font-size: 19.5px; letter-spacing: 0.2px; white-space: nowrap; }
  .claim svg { width: 34px; height: 34px; margin-right: 14px; flex: none; }
  .endorsements { position: absolute; left: 22px; top: 297px; font-size: 19.5px; line-height: 32px; }
</style>
</head>
<body>
<main class="package">
  <svg class="backdrop" width="886" height="1200" viewBox="0 0 886 1200">
    <defs>
      <linearGradient id="sorghumTone" x1="0" y1="1" x2="1" y2="0">
        <stop offset="0" stop-color="var(--sorghum-light)"/>
        <stop offset="1" stop-color="var(--sorghum)"/>
      </linearGradient>
      <linearGradient id="rotiTone" x1="0" y1="0" x2="0" y2="1">
        <stop offset="0" stop-color="var(--roti-light)"/>
        <stop offset="1" stop-color="var(--roti)"/>
      </linearGradient>
    </defs>
    <path d="M0 0 H528 Q470 80 420 180 Q380 245 300 250 Q200 258 120 215 Q60 175 40 95 Q28 40 0 30 Z" fill="var(--blush)"/>
    <rect x="180" y="54" width="188" height="196" rx="70" fill="var(--rose)" opacity="0.75"/>
    <path d="M453 0 H886 V280 Q760 285 690 230 Q640 190 560 210 Q470 230 455 180 Q440 130 520 70 Q560 35 453 0 Z" fill="var(--lilac)"/>
    <path d="M730 50 Q800 30 870 55 Q895 110 860 165 Q800 190 740 170 Q700 120 730 50 Z" fill="var(--teal)"/>
    <path d="M0 105 Q60 50 150 40 Q260 35 340 60 Q420 80 470 55 Q505 35 523 0" fill="none" stroke="var(--teal)" stroke-width="3"/>
    <rect x="0" y="812" width="135" height="179" rx="40" fill="var(--mauve)" opacity="0.7"/>
    <path d="M0 880 Q150 900 240 980 Q330 1050 380 1130 Q390 1200 300 1200 H0 Z" fill="var(--lilac)" opacity="0.9"/>
    <path d="M418 1200 Q415 1150 470 1140 Q560 1130 615 1150 V1200 Z" fill="var(--peach)"/>
    <rect x="40" y="232" width="590" height="470" rx="24" fill="url(#sorghumTone)" opacity="0.85"
          role="img" aria-label="Photograph of a large red sorghum grain head on its stalk"/>
    <rect x="626" y="384" width="240" height="322" rx="24" fill="url(#sorghumTone)" opacity="0.85"
          role="img" aria-label="Photograph of a smaller red sorghum grain head"/>
    <rect x="54" y="955" width="276" height="186" rx="24" fill="url(#rotiTone)"
          role="img" aria-label="Photograph of a stack of soft roti flatbreads"/>
  </svg>

  <h1>
    <span class="title-line title-plain">Plain</span>
    <span class="title-line title-flour">Flour</span>
    <span class="title-line title-gf">GLUTEN FREE</span>
  </h1>

  <p class="benefits">
    0% Saturated Fat only 1% Total fat,<br>
    Cholesterol Free, Very Low Sodium,<br>
    Good Source of Dietary Fiber.<br>
    Weight management.<br>
    Perfect for Gluten free lifestyle.
  </p>

  <p class="net-weight">NET WT:<br>075oz 500gm</p>

  <aside class="claims-panel">
    <ul class="claims">
      <li class="claim"><svg viewBox="0 0 34 34"><circle cx="17" cy="17" r="15" fill="none" stroke="#fff" stroke-width="2"/><path d="M7 18 Q17 12 27 18 Q17 26 7 18 Z" fill="#fff"/></svg>100% ORGANIC</li>
      <li class="claim"><svg viewBox="0 0 34 34"><circle cx="17" cy="17" r="15" fill="none" stroke="#fff" stroke-width="2"/><path d="M17 8 V27 M17 14 L12 11 M17 14 L22 11 M17 19 L12 16 M17 19 L22 16" stroke="#fff" stroke-width="2"/></svg>100% GLUTEN FREE</li>
      <li class="claim"><svg viewBox="0 0 34 34"><circle cx="17" cy="17" r="15" fill="none" stroke="#fff" stroke-width="2"/><text x="17" y="16" font-size="8" fill="#fff" text-anchor="middle" font-family="Oswald, sans-serif">LOW</text><text x="17" y="25" font-size="8" fill="#fff" text-anchor="middle" font-family="Oswald, sans-serif">GI</text></svg>LOW GI</li>
      <li class="claim"><svg viewBox="0 0 34 34"><circle cx="17" cy="17" r="15" fill="none" stroke="#fff" stroke-width="2"/><path d="M10 11 L16 25 L24 9 Q14 12 16 25" fill="none" stroke="#fff" stroke-width="2"/></svg>VEGAN</li>
      <li class="claim"><svg viewBox="0 0 34 34"><circle cx="17" cy="17" r="15" fill="none" stroke="#fff" stroke-width="2"/><ellipse cx="17" cy="17" rx="5" ry="9" transform="rotate(40 17 17)" fill="#fff"/></svg>SOY FREE</li>
      <li class="claim"><svg viewBox="0 0 34 34"><circle cx="17" cy="17" r="15" fill="none" stroke="#fff" stroke-width="2"/><path d="M14 8 H20 V12 L22 15 V26 H12 V15 L14 12 Z" fill="#fff"/></svg>DAIRY FREE</li>
    </ul>
    <p class="endorsements">ALLERGENS FREE<br>GRAINWELL ALLIANCE</p>
  </aside>
</main>
</body>
</html>
```